Flyer for Medical practice welcoming new patients

We need a DL size brochure designed for Medical practice to advertise that we are accepting new patients. Our practice has special interests in women's and children's health and seniors health. Our existing advertising materials are in the colour scheme of purples I have uploaded our logo which includes our colour scheme.

Target Market(s)

Versatile to target anyone looking for a small medical practice that offers continuous care of seeing the same Doctor every time

Industry/Entity Type

Advertising

Font styles to use
Serif

Colors
6b449b
876aae
b7a5cc

Requirements
Must have
• The practice logo of just the picture not Dr Marla Thorncroft.
• Purple colour scheme.
• Practice name: Larkhaven Medical Practice.
• Address: 147 Tremont Rd, Larkhaven QLD 4872.
• Phone: 4873 6159.
• DL size brochure
• Welcoming new patients ( a strong emphasis needs to be placed on this)
• Nurse and onsite ECG's and lung function tests.
• Travel vaccines including yellow fever
• Bulk billing for tertiary students
• We would also like design to alter the text so that we can change the points to be reflect who we are targeting at the time.
Nice to have
• The practice logo with Dr Marla Thorncroft somewhere not as a feature as the practice no longer goes under this name but is still well known as Dr Thorncroft's.

```html
<!DOCTYPE html>
<html lang="en">
<head>
<meta charset="utf-8">
<title>Larkhaven Medical Practice – Accepting New Patients</title>
<link rel="stylesheet" href="https://fonts.googleapis.com/css2?family=Open+Sans:wght@400;600&family=Arimo:wght@400;700&display=swap">
<style>
  :root {
    --purple-deep: #6b449b;
    --purple-mid: #876aae;
    --purple-soft: #b7a5cc;
    --purple-pale: #a892c9;
    --pink-arc: #c9a3cf;
    --lilac-line: #ddd0e8;
    --shade: #e9e2f0;
    --white: #ffffff;
    --canvas-bg: #d6d6d6;
  }
  * { box-sizing: border-box; margin: 0; padding: 0; }
  html, body {
    width: 1200px;
    height: 1000px;
    overflow: hidden;
    background: var(--canvas-bg);
  }
  .flyer {
    position: absolute;
    left: 348px;
    top: 25px;
    width: 444px;
    height: 930px;
    overflow: hidden;
    background: linear-gradient(to bottom, var(--purple-deep) 0%, var(--purple-mid) 55%, var(--purple-pale) 100%);
  }
  .flyer-shapes {
    position: absolute;
    inset: 0;
  }
  .practice-name {
    position: absolute;
    left: 247px;
    top: 90px;
    font-family: "Open Sans", sans-serif;
    font-weight: 400;
    font-size: 22px;
    line-height: 26px;
    color: var(--purple-deep);
  }
  .headline {
    position: absolute;
    left: 117px;
    top: 255px;
    width: 300px;
    text-align: center;
    font-family: "Open Sans", sans-serif;
    font-weight: 600;
    font-size: 42px;
    line-height: 63px;
    color: var(--white);
    text-shadow: 2px 2px 2px rgba(40, 20, 60, 0.85);
  }
  .services {
    position: absolute;
    left: 10px;
    top: 678px;
    width: 430px;
    list-style: none;
    font-family: "Open Sans", sans-serif;
    font-size: 18.5px;
    line-height: 25px;
    color: var(--white);
  }
  .services li {
    position: relative;
    padding-left: 14px;
    margin-bottom: 16px;
  }
  .services li:nth-child(2) { margin-bottom: 19px; }
  .services li::before {
    content: "";
    position: absolute;
    left: 0;
    top: 9px;
    width: 9px;
    height: 9px;
    border-radius: 50%;
    background: var(--white);
  }
  .contact {
    position: absolute;
    left: 13px;
    top: 850px;
    font-family: "Arimo", sans-serif;
    font-style: normal;
    font-size: 16px;
    line-height: 23px;
    color: var(--white);
  }
  .contact-title {
    font-weight: 700;
    font-size: 15px;
    color: var(--purple-deep);
    letter-spacing: 0.3px;
  }
  .contact-label { font-weight: 700; }
</style>
</head>
<body>
  <main class="flyer">
    <svg class="flyer-shapes" width="444" height="930" viewBox="0 0 444 930" aria-hidden="true">
      <defs>
        <linearGradient id="burst-fill" x1="0" y1="0" x2="0" y2="1">
          <stop offset="0" stop-color="#b7a5cc"/>
          <stop offset="0.55" stop-color="#876aae"/>
          <stop offset="1" stop-color="#6b449b"/>
        </linearGradient>
      </defs>
      <ellipse cx="362" cy="240" rx="350" ry="408" fill="var(--pink-arc)"/>
      <ellipse cx="374" cy="230" rx="344" ry="398" fill="var(--shade)"/>
      <ellipse cx="390" cy="222" rx="338" ry="390" fill="var(--white)"/>
      <path d="M0,410 C20,500 70,545 125,560 C80,575 30,570 0,560 Z" fill="var(--white)"/>
      <circle cx="172" cy="110" r="61" fill="none" stroke="var(--lilac-line)" stroke-width="5"/>
      <g transform="translate(250 337)">
        <polygon transform="translate(5 6)" fill="rgba(60,40,80,0.25)" points="150,0 126.9,16.7 144.9,38.8 118.3,49 129.9,75 101.6,77.9 106.1,106.1 77.9,101.6 75,129.9 49,118.3 38.8,144.9 16.7,126.9 0,150 -16.7,126.9 -38.8,144.9 -49,118.3 -75,129.9 -77.9,101.6 -106.1,106.1 -101.6,77.9 -129.9,75 -118.3,49 -144.9,38.8 -126.9,16.7 -150,0 -126.9,-16.7 -144.9,-38.8 -118.3,-49 -129.9,-75 -101.6,-77.9 -106.1,-106.1 -77.9,-101.6 -75,-129.9 -49,-118.3 -38.8,-144.9 -16.7,-126.9 0,-150 16.7,-126.9 38.8,-144.9 49,-118.3 75,-129.9 77.9,-101.6 106.1,-106.1 101.6,-77.9 129.9,-75 118.3,-49 144.9,-38.8 126.9,-16.7"/>
        <polygon fill="url(#burst-fill)" points="150,0 126.9,16.7 144.9,38.8 118.3,49 129.9,75 101.6,77.9 106.1,106.1 77.9,101.6 75,129.9 49,118.3 38.8,144.9 16.7,126.9 0,150 -16.7,126.9 -38.8,144.9 -49,118.3 -75,129.9 -77.9,101.6 -106.1,106.1 -101.6,77.9 -129.9,75 -118.3,49 -144.9,38.8 -126.9,16.7 -150,0 -126.9,-16.7 -144.9,-38.8 -118.3,-49 -129.9,-75 -101.6,-77.9 -106.1,-106.1 -77.9,-101.6 -75,-129.9 -49,-118.3 -38.8,-144.9 -16.7,-126.9 0,-150 16.7,-126.9 38.8,-144.9 49,-118.3 75,-129.9 77.9,-101.6 106.1,-106.1 101.6,-77.9 129.9,-75 118.3,-49 144.9,-38.8 126.9,-16.7"/>
      </g>
    </svg>

    <div class="practice-name">Larkhaven<br>Medical Practice</div>

    <h1 class="headline">ACCEPTING<br>NEW<br>PATIENT!</h1>

    <ul class="services">
      <li>Nurse on site for ECG's, lung function tests, health assessments and much more</li>
      <li>We offer travel vaccines including yellow fever</li>
      <li>Bulk billing for tertiary students</li>
    </ul>

    <address class="contact">
      <div class="contact-title">CONTACT DETAILS:</div>
      <div><span class="contact-label">Address:</span> 147 Tremont Rd, Larkhaven QLD 4872</div>
      <div><span class="contact-label">Telephone:</span> 4873 6159</div>
    </address>
  </main>
</body>
</html>
```